Voltarey - Flyer design

Description -
Motorhome and Caravan EWOFs
Recreational Vehicles (such as caravans, motorhomes, RVs, Boats etc) and Relocatable buildings that can be connected to an electricity supply must be regularly checked for electrical safety. An EWOF needs to be issued every 4 years.
Pre-purchase house inspections
A pre-purchase electrical inspection prior to buying a home can be used to identify any dangerous and unsafe electrical parts of the installation that may be costly to repair once the property has been purchased. Giving you peace of mind when buying your new home.
High risk Electrical inspections
All Prescribed Electrical Work that falls under the High Risk category must be inspected by a Registered Electrical Inspector and have a Record of Inspection certificate issued.
Electric Vehicle Chargers
Any electrical vehicle charger that can be accessed by the public (ie in a non-domestic situation) must be periodically inspected and certified every 12 months.
General Electrical Services
Domestic and commercial - We do new builds, Renovations, Maintenance and more!
Dean Fowler - Electrician and Electrical Inspector
Ph - 0227839152
Dean@voltarey.co.nz
Auckland
------
I also want there to be a few symbols similar to the files I have attached.
The main areas that I am hoping to find work is with caravans/motohomes and EV car chargers so these symbols are quite important.
Thanks so much

```html
<!DOCTYPE html>
<html lang="en">
<head>
<meta charset="utf-8">
<title>Voltarey – Flyer</title>
<link rel="stylesheet" href="https://fonts.googleapis.com/css2?family=Montserrat:wght@700;800;900&family=Poppins:wght@400;500;600;700&display=swap">
<style>
  :root{
    --green:#8dc63f;
    --green-text:#6aab2e;
    --ink:#2e2e2e;
    --white:#ffffff;
  }
  *{margin:0;padding:0;box-sizing:border-box}
  html,body{width:945px;height:1200px;overflow:hidden;background:var(--white)}
  .flyer{position:relative;width:945px;height:1200px;overflow:hidden;background:var(--white);font-family:'Poppins',sans-serif;color:var(--ink)}
  .abs{position:absolute}
  .left-column{left:0;top:0;width:417px;height:1200px;background:var(--green)}
  .hero-frame{left:417px;top:182px;width:460px;height:324px;background:var(--green)}
  .corner-frames{right:0;top:0}
  .brand-name{left:80px;top:88px;font-family:'Poppins',sans-serif;font-weight:600;font-size:36px;line-height:40px;color:#4a4a4a;letter-spacing:-0.5px}
  .hero-panel{left:97px;top:192px;width:771px;height:304px;background:linear-gradient(90deg,#1f1f1f,#3a3a3a 70%,#2a2a2a)}
  .plug-photo{left:0;top:176px;width:172px;height:330px;background:radial-gradient(ellipse at 60% 40%,#3a3a3a,#1a1a1a 60%,rgba(26,26,26,0) 72%)}
  .worker-photo{left:585px;top:223px;width:283px;height:273px;background:linear-gradient(135deg,#6d6d6d,#4a4a4a 45%,#2f3a52 70%,#8b6a43)}
  .headline{left:197px;top:238px;font-family:'Montserrat',sans-serif;font-weight:800;font-size:33px;line-height:36px;color:var(--white);letter-spacing:0.2px}
  .headline .accent{color:var(--green)}
  .dots{left:198px;top:390px;font-family:'Montserrat',sans-serif;font-size:14px;color:var(--green);letter-spacing:1px;font-weight:900}
  .subhead{left:197px;top:411px;font-weight:500;font-size:18px;line-height:23px;color:var(--white)}
  .thumb{top:513px;width:149px;height:130px;border-right:5px solid var(--green);border-bottom:5px solid var(--green)}
  .thumb-motorhome{left:401px;background:linear-gradient(180deg,#e9eef2 0,#cfc7b5 55%,#6ea04a 75%,#4f8a35)}
  .thumb-campervan{left:568px;background:linear-gradient(180deg,#6f8d5a 0,#b9c2bf 45%,#e4e6e8 60%,#8aa65a 80%)}
  .thumb-boat{left:735px;background:linear-gradient(180deg,#7fb6e6 0,#b9d6ee 40%,#f1f3f5 55%,#3f7fa7 75%,#2d6b93)}
  .section-title{left:76px;top:546px;font-family:'Montserrat',sans-serif;font-weight:800;font-size:35px;line-height:36px;letter-spacing:4px;color:var(--ink)}
  .service-card{left:73px;width:266px;border:3px solid var(--ink);border-right:none;border-radius:12px 0 0 12px}
  .card-ev{top:639px;height:224px}
  .card-general{top:925px;height:224px}
  .card-title{font-family:'Montserrat',sans-serif;font-weight:800;font-size:23px;line-height:27px;color:var(--ink)}
  .card-body{font-size:13.5px;line-height:16.5px;color:var(--ink)}
  .card-sub{font-family:'Montserrat',sans-serif;font-weight:800;font-size:14.5px;color:var(--ink)}
  .bullet-list{list-style:none;font-size:13.5px;line-height:21px}
  .bullet-list li{position:relative;padding-left:14px}
  .bullet-list li::before{content:"";position:absolute;left:0;top:7px;width:8px;height:8px;border-radius:50%;background:var(--ink)}
  .offer{left:446px;width:440px}
  .offer-icon{position:absolute;left:0;top:-4px}
  .offer-title{margin-left:76px;font-family:'Montserrat',sans-serif;font-weight:700;font-size:18.5px;color:#3a3a3a;white-space:nowrap}
  .offer-title .accent{color:var(--green-text)}
  .offer-body{margin-left:76px;margin-top:5px;width:360px;font-size:12.4px;line-height:14.8px;color:#222}
  .contact-heading{left:452px;top:1052px;font-family:'Montserrat',sans-serif;font-weight:800;font-size:30px;color:#333}
  .name-bar{left:456px;top:1100px;height:38px;display:flex}
  .name-bar .name{background:#333;color:var(--white);font-family:'Montserrat',sans-serif;font-weight:800;font-size:19px;padding:0 10px;line-height:38px;white-space:nowrap;border-radius:3px 0 0 3px}
  .name-bar .role{background:var(--green);color:#2c2c2c;font-family:'Montserrat',sans-serif;font-weight:700;font-size:10.5px;line-height:13px;padding:6px 10px;width:137px;border-radius:0 3px 3px 0}
  .contact-line{left:454px;top:1148px;display:flex;align-items:center;gap:6px;font-size:15px;color:#222;white-space:nowrap}
  .contact-line .item{display:flex;align-items:center;gap:6px;margin-right:10px}
</style>
</head>
<body>
<div class="flyer">
  <div class="abs left-column"></div>
  <div class="abs hero-frame"></div>

  <svg class="abs corner-frames" width="180" height="165" viewBox="0 0 180 165" aria-hidden="true">
    <g fill="none" stroke="#d0d0d0" stroke-width="6">
      <path d="M177 11 H83 V93 H177"/>
      <path d="M72 54 H3 V122 H72"/>
      <path d="M125 112 H83 V163 H125"/>
    </g>
  </svg>

  <div class="abs brand-name">Voltarey</div>

  <div class="abs hero-panel"></div>
  <div class="abs worker-photo" role="img" aria-label="Photo of an electrician in a hard hat wiring sockets into a grey brick wall"></div>
  <div class="abs plug-photo" role="img" aria-label="Photo of a black power plug with a curling cable"></div>

  <div class="abs headline">YOUR TRUSTED<br>PARTNER IN<br><span class="accent">ELECTRICAL SAFETY<br>AND COMPLIANCE</span></div>
  <div class="abs dots">•••••</div>
  <div class="abs subhead">Your Trusted Experts in Electrical<br>Compliance and Repairs</div>

  <div class="abs thumb thumb-motorhome" role="img" aria-label="Photo of a vintage motorhome parked on grass"></div>
  <div class="abs thumb thumb-campervan" role="img" aria-label="Photo of a white campervan on a grassy field"></div>
  <div class="abs thumb thumb-boat" role="img" aria-label="Photo of a white motor boat moored in a marina"></div>

  <div class="abs section-title">OUR<br>SERVICES</div>

  <div class="abs service-card card-ev"></div>
  <svg class="abs" style="left:300px;top:628px" width="50" height="24" viewBox="0 0 50 24" aria-hidden="true">
    <rect x="0" y="10" width="18" height="3" fill="#2e2e2e"/>
    <path d="M18 5 h6 v-2 h8 a6 6 0 0 1 6 6 v6 a6 6 0 0 1 -6 6 h-8 v-2 h-6z" fill="#2e2e2e"/>
    <rect x="38" y="6" width="10" height="3" fill="#2e2e2e"/>
    <rect x="38" y="14" width="10" height="3" fill="#2e2e2e"/>
  </svg>
  <div class="abs card-title" style="left:98px;top:657px">Electric<br>Vehicle<br>Chargers</div>
  <div class="abs card-body" style="left:98px;top:751px;width:245px">Any electrical vehicle charger that can be accessed by the public (ie in a non-domestic situation) must be periodically inspected and certified every 12 months.</div>
  <svg class="abs" style="left:265px;top:838px" width="80" height="56" viewBox="0 0 80 56" aria-hidden="true">
    <path d="M14 22 L22 6 Q24 2 29 2 H51 Q56 2 58 6 L66 22 Q76 24 76 32 V46 H4 V32 Q4 24 14 22Z" fill="#2e2e2e"/>
    <path d="M20 21 L26 9 H54 L60 21Z" fill="var(--green)"/>
    <circle cx="16" cy="32" r="4" fill="var(--green)"/><circle cx="64" cy="32" r="4" fill="var(--green)"/>
    <rect x="8" y="44" width="12" height="11" rx="2" fill="#2e2e2e"/><rect x="60" y="44" width="12" height="11" rx="2" fill="#2e2e2e"/>
  </svg>

  <div class="abs service-card card-general"></div>
  <svg class="abs" style="left:300px;top:914px" width="50" height="24" viewBox="0 0 50 24" aria-hidden="true">
    <rect x="0" y="10" width="18" height="3" fill="#2e2e2e"/>
    <path d="M18 5 h6 v-2 h8 a6 6 0 0 1 6 6 v6 a6 6 0 0 1 -6 6 h-8 v-2 h-6z" fill="#2e2e2e"/>
    <rect x="38" y="6" width="10" height="3" fill="#2e2e2e"/>
    <rect x="38" y="14" width="10" height="3" fill="#2e2e2e"/>
  </svg>
  <div class="abs card-title" style="left:98px;top:945px">General Electrical<br>Services</div>
  <div class="abs card-sub" style="left:98px;top:1000px">Domestic and commercial</div>
  <div class="abs card-body" style="left:101px;top:1025px">We do</div>
  <ul class="abs bullet-list" style="left:101px;top:1046px">
    <li>New builds</li>
    <li>Renovations</li>
    <li>Maintenance<br>and more!</li>
  </ul>
  <svg class="abs" style="left:270px;top:1066px" width="110" height="86" viewBox="0 0 110 86" aria-hidden="true">
    <path d="M38 2 A42 42 0 0 1 38 83" fill="none" stroke="#2e2e2e" stroke-width="3"/>
    <path d="M30 8 L56 30 V66 H4 V30Z" fill="none" stroke="#2e2e2e" stroke-width="4" stroke-linejoin="round"/>
    <path d="M30 14 L51 32 V62 H9 V32Z" fill="none" stroke="#2e2e2e" stroke-width="2"/>
    <circle cx="30" cy="40" r="7" fill="none" stroke="#2e2e2e" stroke-width="2.5"/>
    <rect x="26" y="47" width="8" height="6" fill="#2e2e2e"/>
  </svg>

  <div class="abs offer" style="top:678px">
    <svg class="offer-icon" width="52" height="52" viewBox="0 0 52 52" aria-hidden="true">
      <path d="M4 24 A22 22 0 0 1 48 24" fill="none" stroke="var(--green)" stroke-width="4"/>
      <circle cx="26" cy="29" r="20" fill="#333"/>
      <rect x="15" y="21" width="20" height="13" rx="2" fill="none" stroke="#fff" stroke-width="2"/>
      <rect x="18" y="24" width="5" height="4" fill="#fff"/><rect x="26" y="24" width="5" height="4" fill="#fff"/>
      <circle cx="20" cy="36" r="2.5" fill="#fff"/><circle cx="31" cy="36" r="2.5" fill="#fff"/>
      <path d="M35 30 h4" stroke="#fff" stroke-width="2"/>
    </svg>
    <div class="offer-title">Motorhome and <span class="accent">Caravan EWOFs</span></div>
    <div class="offer-body">Recreational Vehicles (such as caravans, motorhomes, RVs, Boats etc) and Relocatable buildings that can be connected to an electricity supply must be regularly checked for electrical safety. An EWOF needs to be issued every 4 years.</div>
  </div>

  <div class="abs offer" style="top:797px">
    <svg class="offer-icon" width="52" height="52" viewBox="0 0 52 52" aria-hidden="true">
      <path d="M4 24 A22 22 0 0 1 48 24" fill="none" stroke="var(--green)" stroke-width="4"/>
      <circle cx="26" cy="29" r="20" fill="#333"/>
      <path d="M14 29 L24 20 L32 27 M17 27 V37 H26" fill="none" stroke="#fff" stroke-width="2"/>
      <circle cx="31" cy="33" r="5" fill="none" stroke="#fff" stroke-width="2"/>
      <path d="M35 37 L39 41" stroke="#fff" stroke-width="2.5"/>
    </svg>
    <div class="offer-title">Pre-purchase <span class="accent">house inspections</span></div>
    <div class="offer-body">A pre-purchase electrical inspection prior to buying a home can be used to identify any dangerous and unsafe electrical parts of the installation that may be costly to repair once the property has been purchased. Giving you peace of mind when buying your new home.</div>
  </div>

  <div class="abs offer" style="top:933px">
    <svg class="offer-icon" width="52" height="52" viewBox="0 0 52 52" aria-hidden="true">
      <path d="M4 24 A22 22 0 0 1 48 24" fill="none" stroke="var(--green)" stroke-width="4"/>
      <circle cx="26" cy="29" r="20" fill="#333"/>
      <path d="M15 28 L26 18 L37 28" fill="none" stroke="#fff" stroke-width="2"/>
      <circle cx="26" cy="32" r="7" fill="none" stroke="#fff" stroke-width="2"/>
      <path d="M23 29 v3 M29 29 v3 M26 35 v3" stroke="#fff" stroke-width="1.8"/>
    </svg>
    <div class="offer-title">High risk <span class="accent">Electrical inspections</span></div>
    <div class="offer-body">All Prescribed Electrical Work that falls under the High Risk category must be inspected by a Registered Electrical Inspector and have a Record of Inspection certificate issued.</div>
  </div>

  <div class="abs contact-heading">Contact Us Today!</div>
  <div class="abs name-bar">
    <div class="name">DEAN FOWLER</div>
    <div class="role">Electrician and<br>Electrical Inspector</div>
  </div>
  <div class="abs contact-line">
    <span class="item">
      <svg width="16" height="16" viewBox="0 0 16 16" aria-hidden="true"><circle cx="8" cy="8" r="8" fill="var(--green)"/><path d="M5 4 l2 2 -1 1 q1 2 3 3 l1-1 2 2 -1 1 q-5 0 -7-6z" fill="#222"/></svg>
      0227839152
    </span>
    <span class="item">
      <svg width="16" height="16" viewBox="0 0 16 16" aria-hidden="true"><circle cx="8" cy="8" r="8" fill="var(--green)"/><rect x="4" y="5" width="8" height="6" fill="#222"/><path d="M4 5 l4 3 4-3" fill="none" stroke="var(--green)" stroke-width="1"/></svg>
      Dean@voltarey.co.nz
    </span>
    <span class="item">
      <svg width="16" height="16" viewBox="0 0 16 16" aria-hidden="true"><circle cx="8" cy="8" r="8" fill="var(--green)"/><path d="M8 13 L5 8 A3.3 3.3 0 1 1 11 8Z" fill="#222"/><circle cx="8" cy="6.5" r="1.2" fill="var(--green)"/></svg>
      Auckland
    </span>
  </div>
</div>
</body>
</html>
```